Tech business card design

We need an amazing business card design for our new business 'Brakka' a marketing tech startup based in Sydney, Australia. We provide an online marketplace for businesses to search and buy advertising media, connect with service providers and learn more about marketing. We wish to communicate 'cool tech', reliability and professionalism and design based around our logo.

Target Market(s)

Business Owners

Contact Information for Business Card

Name
Position
Email Address
Website
Phone Number

Font styles to use
Other font styles liked:
• Avenir & Avenir Next

Colors

Designer to choose colors to be used in the design.

```html
<!DOCTYPE html>
<html lang="en">
<head>
<meta charset="utf-8">
<title>Brakka Business Card</title>
<link rel="stylesheet" href="https://fonts.googleapis.com/css2?family=Oswald:wght@500&family=Work+Sans:wght@400;700&display=swap">
<style>
  :root {
    --backdrop: #1b1b1b;
    --card: #1e1e1e;
    --card-edge: #2a2a2a;
    --ink: #f4f4f4;
    --ink-soft: #d9d9d9;
  }
  * { margin: 0; padding: 0; box-sizing: border-box; }
  html, body {
    width: 1200px; height: 900px; overflow: hidden;
    background: var(--backdrop);
  }
  .stage {
    width: 1200px; height: 900px;
    display: flex; flex-direction: column; align-items: center; justify-content: center;
    gap: 24px;
  }
  .card {
    position: relative;
    width: 700px; height: 400px;
    background: linear-gradient(135deg, var(--card) 0%, #222 60%, #2b2b2b 100%);
    border: 1px solid var(--card-edge);
    color: var(--ink);
    font-family: "Work Sans", sans-serif;
  }
  .card-front { display: flex; align-items: center; justify-content: center; }
  .brand-name {
    font-family: "Work Sans", sans-serif;
    font-weight: 700;
    font-size: 110px;
    letter-spacing: -2px;
    color: var(--ink);
  }
  .identity {
    position: absolute; left: 130px; top: 140px; width: 210px;
    text-align: right;
  }
  .person-name {
    font-family: "Oswald", sans-serif; font-weight: 500;
    font-size: 32px; letter-spacing: 0.5px; text-transform: uppercase; line-height: 1.1;
  }
  .person-role { font-size: 17px; letter-spacing: 1px; color: var(--ink-soft); margin-top: 2px; }
  .divider {
    position: absolute; left: 366px; top: 140px;
    width: 2px; height: 74px; background: var(--ink);
  }
  .contact-list {
    position: absolute; left: 392px; top: 136px; list-style: none;
  }
  .contact-item {
    display: flex; align-items: center; gap: 14px;
    font-size: 19px; letter-spacing: 1px; line-height: 28px;
  }
  .contact-icon { width: 13px; height: 13px; flex: none; }
  .address {
    position: absolute; left: 150px; bottom: 58px;
    font-size: 20px; letter-spacing: 1px;
  }
</style>
</head>
<body>
<main class="stage">
  <section class="card card-front">
    <span class="brand-name">Brakka</span>
  </section>

  <section class="card card-back">
    <div class="identity">
      <p class="person-name">Daniel Reyes</p>
      <p class="person-role">Director</p>
    </div>
    <span class="divider"></span>
    <ul class="contact-list">
      <li class="contact-item">
        <svg class="contact-icon" viewBox="0 0 16 16" aria-hidden="true"><path d="M4 1l2.5 3-1.5 1.5c1 2.2 2.8 4 5 5L11.5 9 15 11.5 13.5 14.5C7 14 2 9 1.5 2.5z" fill="none" stroke="#f4f4f4" stroke-width="1.4"/></svg>
        +330 5812-3907
      </li>
      <li class="contact-item">
        <svg class="contact-icon" viewBox="0 0 16 16" aria-hidden="true"><rect x="1" y="3" width="14" height="10" fill="none" stroke="#f4f4f4" stroke-width="1.5"/><path d="M1 3l7 5.5L15 3" fill="none" stroke="#f4f4f4" stroke-width="1.5"/></svg>
        info@brakka.com
      </li>
      <li class="contact-item">
        <svg class="contact-icon" viewBox="0 0 16 16" aria-hidden="true"><g fill="none" stroke="#f4f4f4" stroke-width="1.3"><circle cx="8" cy="8" r="6.5"/><ellipse cx="8" cy="8" rx="3" ry="6.5"/><path d="M1.5 8h13M2.5 4.5h11M2.5 11.5h11"/></g></svg>
        www.brakka.com
      </li>
    </ul>
    <p class="address">218 Wattle Lane Sydney, NSW 2000</p>
  </section>
</main>
</body>
</html>
```